High end bathroom & wetroom supply and installation uk company require an A4 folded brochure

We have a website "fernandbrass.com" this shows the market we are aiming at i.e. higher end

The brochure will be a fold out A4 ( three internal pages and front and rear cover) it will have lots of imagery ( we can supply photographs of our projects) and also incorporate a "design sketch" element on the "design" page - the internal pages of the brochure will be headed - page 1 - design, page 2 "supply" - page 3 ' install"
( see website - this will give a better idea)

The brochures purpose is to show potential clients ( private clients / architects / property developers) that we offer a comprehensive design service - a comprehensive supply service - and a professional installation service

We will provide wording - there will only be a few paragraphs - the images are the key to the impact of the brochure which will be printed on high quality gloss heavyweight paper/card
Updates

Apologies for confusion, my fault :-(

The brochure will be an A4 gatefold ( finished size A4) which would indeed be six sides ( inc front and rear covers) 

I'll upload photos etc tomorrow - I like the idea of the text ( which will be very similar to what is on the website) to be laid on top of the image rather than in a separate text box. 

I like the idea of the brochure looking like the website.

Hope that helps - 

this image shows the brochure type

www.printwaveguild.co.uk/assets/images/6PP_A4BrochurePlan.gif

Requirements
Must have
• when the a4 gate fold is open i.e. you are looking at three a4 pages they should be headed as;
page 1 - design
page 2 - supply
page 3 - install

A4 gate fold -A4 finished size

```html
<!DOCTYPE html>
<html lang="en">
<head>
<meta charset="utf-8">
<title>Fern &amp; Brass – Gatefold Brochure Interior</title>
<link href="https://fonts.googleapis.com/css2?family=Marcellus&family=Montserrat:wght@400;600&display=swap" rel="stylesheet">
<style>
  :root {
    --stage: #0b0b0b;
    --paper: #ffffff;
    --column: rgba(92, 97, 101, 0.84);
    --column-top: #7b8084;
    --ink-light: #ffffff;
    --frame: #ffffff;
    --photo-stone-a: #cfc8bb;
    --photo-stone-b: #7d776d;
    --photo-room-a: #b9bcbd;
    --photo-room-b: #4d5256;
    --photo-warm-a: #d9cdb6;
    --photo-warm-b: #8d7f69;
  }
  * { box-sizing: border-box; margin: 0; padding: 0; }
  html, body {
    width: 1200px; height: 957px; overflow: hidden;
    background: var(--stage);
  }
  .spread {
    position: absolute; left: 30px; top: 210px;
    width: 1140px; height: 537px;
    display: flex;
  }
  .page {
    position: relative; width: 380px; height: 537px;
    background: var(--paper); overflow: hidden;
  }
  .page-photo {
    position: absolute; left: 0; right: 0; top: 66px; bottom: 0;
  }
  .page--design .page-photo { background: linear-gradient(160deg, var(--photo-room-a), var(--photo-room-b)); }
  .page--supply .page-photo { background: linear-gradient(170deg, var(--photo-room-a), #6d7275 70%, var(--photo-room-b)); }
  .page--install .page-photo { background: linear-gradient(150deg, var(--photo-stone-a), var(--photo-stone-b)); }

  .text-column {
    position: absolute; left: 0; top: 0; bottom: 0; width: 214px;
    background: linear-gradient(180deg, var(--column-top) 0, var(--column-top) 66px, var(--column) 66px);
    color: var(--ink-light);
    padding: 0 14px;
  }
  .brand {
    display: flex; align-items: center; gap: 5px;
    margin-top: 10px;
    font-family: "Montserrat", sans-serif; font-weight: 600;
    font-size: 7px; letter-spacing: 0.08em; color: var(--ink-light);
  }
  .brand-mark { width: 8px; height: 8px; background: var(--ink-light); }
  .page-heading {
    margin-top: 40px;
    font-family: "Marcellus", serif; font-weight: 400;
    font-size: 25px; letter-spacing: 0.04em; line-height: 1;
    padding-bottom: 5px; border-bottom: 1px solid var(--ink-light);
    display: inline-block;
  }
  .page-copy {
    margin-top: 14px;
    font-family: "Montserrat", sans-serif; font-weight: 400;
    font-size: 6.6px; line-height: 8.5px;
  }
  .page-copy p { margin-bottom: 7px; }
  .page-copy strong { font-weight: 600; }
  .page-copy .brand-item { margin-bottom: 5px; }

  .thumb {
    position: absolute; right: 14px; width: 122px; height: 80px;
    border: 3px solid var(--frame);
    box-shadow: 0 1px 3px rgba(0,0,0,0.35);
  }
  .thumb--upper { top: 14px; }
  .thumb--lower { top: 106px; }
  .tone-stone { background: linear-gradient(135deg, var(--photo-stone-a), var(--photo-stone-b)); }
  .tone-room { background: linear-gradient(135deg, var(--photo-room-a), var(--photo-room-b)); }
  .tone-warm { background: linear-gradient(135deg, var(--photo-warm-a), var(--photo-warm-b)); }
</style>
</head>
<body>
<main class="spread">

  <section class="page page--design">
    <div class="page-photo" role="img" aria-label="Photograph of a designed bathroom with freestanding bath, plant and LED accent lighting under a sloped ceiling"></div>
    <div class="thumb thumb--upper tone-room" role="img" aria-label="Photograph of a bathroom with freestanding bath and heated towel rail"></div>
    <div class="thumb thumb--lower tone-stone" role="img" aria-label="Photograph of a stone-tiled bathroom with built-in bath"></div>
    <div class="text-column">
      <div class="brand"><span class="brand-mark"></span>FERN &amp; BRASS</div>
      <h2 class="page-heading">&gt;DESIGN</h2>
      <div class="page-copy">
        <p>The importance of the design process cannot be overstated. A professionally designed bathroom will be easier to install, it will be more practical and visually appealing. You will also know before work starts that everything will actually fit.</p>
        <p>We have invested in the highest quality CAD software (and the computers to run it effectively). In the hands of our skilled bathroom and wetroom designers you will be able to see just how your bathroom will look on completion.</p>
        <p>You will be able to discuss your own ideas more easily having seen a 3D image of the room and at this stage changes can be easily implemented.</p>
        <p>We offer a free design service for clients who are interested in our installation service. If you have your own installer (or your builder uses has his own) we charge a small design fee which is fully refundable upon placement of an order for the bathroom equipment.</p>
        <p>A <strong>Fern &amp; Brass</strong> designed bathroom or wetroom has a distinct timeless appearance. We incorporate innovative features into our designs, these can include clever storage ideas and the use of subtle but effective LED accent lighting.</p>
        <p>We use a lot of natural products in our bathrooms and are also able to produce bespoke items i.e. furniture, which we manufacture ourselves.</p>
      </div>
    </div>
  </section>

  <section class="page page--supply">
    <div class="page-photo" role="img" aria-label="Photograph of a showroom bathroom with freestanding bath, pedestal basin and glass screen"></div>
    <div class="thumb thumb--upper tone-warm" role="img" aria-label="Photograph of a stone vessel basin on a marble counter"></div>
    <div class="thumb thumb--lower tone-warm" role="img" aria-label="Photograph of twin stone basins on a wooden vanity"></div>
    <div class="text-column">
      <div class="brand"><span class="brand-mark"></span>FERN &amp; BRASS</div>
      <h2 class="page-heading">&gt;SUPPLY</h2>
      <div class="page-copy">
        <p>At our bathroom showroom in Ashcombe we display a number of well-known brands, we also display some not so well-known brands, what they all have in common is quality. We also manufacture our own bespoke range of solid wood furniture. We offer excellent discounts to both trade and retail on a wide range of products.</p>
        <p class="brand-item"><strong>ALPENKERAM</strong>: Sanitaryware and furniture from Switzerland – excellent quality at affordable prices.</p>
        <p class="brand-item"><strong>RHEINQUELL</strong>: Brassware (taps and showers) from Germany – precision and quality.</p>
        <p class="brand-item"><strong>WOLDGRAIN</strong>: Beautiful solid oak and walnut furniture – made in the UK. <strong>NORDVIK</strong>: Stunning and practical – high end furniture and baths from Sweden.</p>
        <p class="brand-item"><strong>FONTELLI</strong>: Exceptionally high quality brassware from Italy.</p>
        <p class="brand-item"><strong>FERNOAK</strong>: Our own bespoke range of furniture.</p>
        <p>ASHBY &amp; LOWE: Beautiful British made bathrooms.</p>
        <p>We are able to read architects plans (or your own drawings) and together with your thoughts we can compile a list of suitable products for you. This can save you hours of searching for items that will fit and are within your budget. If you have your own installer and are looking for advice on anything from a complete bathroom or maybe just a mirror cabinet we are glad to help. If you have been searching and found nothing that quite fits the bill or maybe you need non-standard furniture sizes or you need a bespoke glass shower screen, then come in and see us as we will be able to help.</p>
      </div>
    </div>
  </section>

  <section class="page page--install">
    <div class="page-photo" role="img" aria-label="Photograph of a person relaxing in a freestanding bath in a natural stone wetroom"></div>
    <div class="thumb thumb--upper tone-stone" role="img" aria-label="Photograph of a stone basin against a tiled wall"></div>
    <div class="thumb thumb--lower tone-room" role="img" aria-label="Photograph of an oval bath beside a wall-mounted screen"></div>
    <div class="text-column">
      <div class="brand"><span class="brand-mark"></span>FERN &amp; BRASS</div>
      <h2 class="page-heading">&gt;INSTALL</h2>
      <div class="page-copy">
        <p>At <strong>Fern &amp; Brass</strong> you can be assured of the highest standards of service. We have over 25 years of experience in the plumbing/heating/bathroom industry and are specialist wetroom installers.</p>
        <p>You will be delighted with the exceptionally high standard of our workmanship and our attention to detail. We relish a challenging project and are full of inspirational ideas that will set your project apart.</p>
        <p>We design and install all types of bathrooms – and we specialise in wetrooms and the use of natural stone. Wetrooms are fast becoming 'the way to go' as far as luxury showers are concerned, we have many full size wetroom displays in our showroom. We manufacture our own range of furniture that can be tailor made to suit whatever space you have available in your bathroom.</p>
        <p>We also manufacture bespoke natural stone surfaces or natural stone accent pieces for a truly unique room.</p>
        <p>We love natural stone and have many years' experience in its installation. Natural stone is an aspirational material and has a timeless and elegant appearance that will delight each and every time you walk into your bathroom or wetroom.</p>
        <p>We have full size displays in our showroom to show you exactly how natural stone could enhance the look and feel of your home.</p>
      </div>
    </div>
  </section>

</main>
</body>
</html>
```